Framework, Visual of our 6 phase process of working with clients

We are an epidemiology consulting firm and need a visual that describes our 6 phase process of how our clients work with us. This will be used in marketing and sales to help potential client understand what to expect when working with us. A visual of our framework will also help us demonstrate authority and more easily explain our process in the sales process. Please message me if you have any questions.

Include our website somewhere: DrMBFolwell.com

Target Market(s)

Large Nonprofit organization leaders

Industry/Entity Type

Health, Public Health, Epidemiology

Font styles to use
Serif

Requirements
Must have
• Please use brand colors: #56588C, #F28444 you can also use #F2E088, #F24C27, #0D0D0D

```html
<!DOCTYPE html>
<html lang="en">
<head>
<meta charset="utf-8">
<title>The DrMBFolwell Framework</title>
<link rel="stylesheet" href="https://fonts.googleapis.com/css2?family=Playfair+Display:wght@600;700&family=Poppins:wght@400;500;600&display=swap">
<style>
  :root {
    --purple: #56588C;
    --orange: #F28444;
    --red-orange: #F24C27;
    --ink: #0D0D0D;
    --text: #2b2b35;
    --white: #ffffff;
    --page: #e7e7e9;
  }
  * { box-sizing: border-box; margin: 0; padding: 0; }
  html, body { width: 871px; height: 1200px; overflow: hidden; }
  body { background: var(--page); font-family: "Poppins", sans-serif; position: relative; }

  .sheet { position: absolute; left: 68px; top: 80px; width: 728px; height: 1030px; background: var(--white); overflow: hidden; }
  .backdrop { position: absolute; inset: 0; }

  .left-panel { position: absolute; left: 0; top: 0; width: 380px; height: 1030px; color: var(--white); }
  .title { position: absolute; left: 60px; top: 278px; font-family: "Playfair Display", serif; font-weight: 700; font-size: 21px; line-height: 26px; white-space: nowrap; }
  .title-band { position: absolute; left: 0; top: 340px; width: 377px; height: 60px; background: var(--orange); border-radius: 0 30px 30px 0; }
  .title-band h2 { position: absolute; left: 60px; top: 16px; font-family: "Playfair Display", serif; font-weight: 700; font-size: 20px; white-space: nowrap; }
  .intro, .body-text, .reasons { position: absolute; left: 60px; width: 318px; font-size: 10.6px; line-height: 13.6px; letter-spacing: -0.15px; }
  .intro { top: 418px; }
  .section-heading { position: absolute; left: 60px; font-family: "Playfair Display", serif; font-weight: 700; font-size: 16px; line-height: 20px; white-space: nowrap; }
  .section-heading::after { content: ""; display: block; width: 158px; height: 1px; background: rgba(255,255,255,.7); margin-top: 6px; }
  .reasons { top: 693px; }
  .reasons p { margin-bottom: 12.5px; }
  .reasons strong, .intro strong, .body-text strong { font-weight: 600; }
  .email-button { position: absolute; left: 58px; top: 966px; width: 226px; height: 31px; background: var(--orange); border-radius: 16px; display: flex; align-items: center; justify-content: center; gap: 8px; font-size: 10.5px; color: var(--white); }

  .brand { position: absolute; left: 484px; top: 52px; display: flex; align-items: center; gap: 7px; font-weight: 600; font-size: 21px; color: var(--purple); }
  .brand-dot { width: 16px; height: 16px; border-radius: 50%; background: var(--orange); }

  .phase-pill { position: absolute; height: 32px; right: 63px; background: var(--purple); border-radius: 0 16px 16px 0; color: var(--white); font-family: "Playfair Display", serif; font-weight: 700; font-size: 13px; letter-spacing: -0.2px; line-height: 32px; white-space: nowrap; }
  .phase-number { position: absolute; width: 36px; height: 36px; border-radius: 50%; background: var(--orange); border: 3px solid var(--white); color: var(--white); font-size: 14px; font-weight: 500; display: flex; align-items: center; justify-content: center; }
  .phase-sub { position: absolute; font-weight: 600; font-size: 11.5px; color: var(--text); white-space: nowrap; }
  .phase-list { position: absolute; list-style: none; font-size: 9.5px; line-height: 14.8px; color: var(--text); }
  .phase-list li { position: relative; padding-left: 10px; }
  .phase-list li::before { content: ""; position: absolute; left: 0; top: 6px; width: 4px; height: 4px; border-radius: 50%; background: var(--purple); }
</style>
</head>
<body>
<main class="sheet">
  <svg class="backdrop" width="728" height="1030" viewBox="0 0 728 1030">
    <defs>
      <clipPath id="panel-shape"><path d="M0 0 H352 C395 300 395 700 347 1030 H0 Z"/></clipPath>
      <linearGradient id="photo-tone" x1="0" y1="0" x2="0" y2="1">
        <stop offset="0" stop-color="#8c7468"/>
        <stop offset="0.45" stop-color="#6b5e6e"/>
        <stop offset="1" stop-color="#56588C"/>
      </linearGradient>
    </defs>
    <path d="M0 0 H352 C395 300 395 700 347 1030 H0 Z" fill="var(--purple)"/>
    <g clip-path="url(#panel-shape)" role="img" aria-label="Photo of a diverse team joining hands in celebration in a bright office">
      <rect x="0" y="0" width="420" height="300" fill="url(#photo-tone)"/>
    </g>
    <path d="M360 0 C403 300 403 700 355 1030" fill="none" stroke="var(--red-orange)" stroke-width="5"/>
  </svg>

  <section class="left-panel">
    <h1 class="title">Transforming Health Data<br>into Community Impact:</h1>
    <div class="title-band"><h2>The DrMBFolwell Framework</h2></div>
    <p class="intro"><strong>DrMBFolwell LLC</strong> is an epidemiology consulting firm that supports large nonprofit organizations and government agencies that serve black, indigenous, and people of color commonly referred to as BIPOC communities. Our diverse team of innovative global public health professionals are ready to serve your organization by helping you address your most pressing challenges.</p>

    <h3 class="section-heading" style="top:526px">Our Approach</h3>
    <p class="body-text" style="top:566px">At <strong>DrMBFolwell LLC</strong>, we believe in transforming health data into actionable insights for BIPOC communities. Our proven six-phase partnership model ensures your organization's success in communicating vital health information effectively.</p>

    <h3 class="section-heading" style="top:652px">Why Partner With Us?</h3>
    <div class="reasons">
      <p><strong>Expertise:</strong> Our diverse team of innovative global public health professionals, specialized in epidemiology and health communication</p>
      <p><strong>Impact:</strong> Proven track record of transforming complex health data into accessible information</p>
      <p><strong>Innovation:</strong> Custom solutions tailored to BIPOC community needs</p>
      <p><strong>Partnership:</strong> Collaborative approach ensuring lasting results</p>
    </div>

    <h3 class="section-heading" style="top:868px">Ready to Transform Your<br>Health Communication?</h3>
    <p class="body-text" style="top:928px">Contact us to begin your journey toward more effective, equitable health communication.</p>

    <div class="email-button">
      <svg width="15" height="11" viewBox="0 0 15 11"><rect x="0.75" y="0.75" width="13.5" height="9.5" rx="1" fill="none" stroke="#fff" stroke-width="1.2"/><path d="M1 1.5 L7.5 6 L14 1.5" fill="none" stroke="#fff" stroke-width="1.2"/></svg>
      <span>support@drmbfolwell.com</span>
    </div>
  </section>

  <div class="brand"><span class="brand-dot"></span><span>DrMBFolwell</span></div>

  <div class="phase-pill" style="left:357px;top:97px;padding-left:50px">Phase 1: Discovery &amp; Vision Alignment</div>
  <div class="phase-number" style="left:349px;top:95px">1</div>
  <h4 class="phase-sub" style="left:407px;top:138px">Building the Foundation for Success</h4>
  <ul class="phase-list" style="left:409px;top:158px;width:240px">
    <li>Deep-dive exploration of your organization's unique challenges and opportunities</li>
    <li>Strategic alignment of goals and expectations</li>
    <li>Custom-tailored solution design</li>
    <li>Clear roadmap development with defined milestones</li>
  </ul>

  <div class="phase-pill" style="left:387px;top:260px;padding-left:48px">Phase 2: Partnership Launch</div>
  <div class="phase-number" style="left:379px;top:258px">2</div>
  <h4 class="phase-sub" style="left:434px;top:300px">Where Science Meets Service</h4>
  <ul class="phase-list" style="left:435px;top:320px;width:230px">
    <li>Formation of dedicated project team</li>
    <li>Establishment of collaborative workflow</li>
    <li>Comprehensive data gathering</li>
    <li>Strategic timeline planning</li>
    <li>Stakeholder engagement and vision capture</li>
  </ul>

  <div class="phase-pill" style="left:407px;top:408px;padding-left:47px">Phase 3: Expert Execution</div>
  <div class="phase-number" style="left:397px;top:406px">3</div>
  <h4 class="phase-sub" style="left:451px;top:448px">Where Science Meets Service</h4>
  <ul class="phase-list" style="left:451px;top:468px;width:210px">
    <li>Our specialized team begins the transformation process:</li>
    <li>In-depth research and analysis</li>
    <li>Content development and refinement</li>
    <li>Data interpretation and visualization</li>
    <li>Plain language translation of complex health information</li>
  </ul>

  <div class="phase-pill" style="left:410px;top:588px;padding-left:43px;font-size:12.5px">Phase 4: Collaborative Refinement</div>
  <div class="phase-number" style="left:399px;top:586px">4</div>
  <h4 class="phase-sub" style="left:453px;top:628px">Ensuring Perfect Alignment</h4>
  <ul class="phase-list" style="left:455px;top:648px;width:210px">
    <li>Presentation of initial frameworks</li>
    <li>Interactive feedback sessions</li>
    <li>Draft review and optimization</li>
    <li>Stakeholder input integration</li>
  </ul>

  <div class="phase-pill" style="left:400px;top:722px;padding-left:45px">Phase 5: Impact Delivery</div>
  <div class="phase-number" style="left:388px;top:720px">5</div>
  <h4 class="phase-sub" style="left:442px;top:762px">Bringing Vision to Reality</h4>
  <ul class="phase-list" style="left:444px;top:782px;width:210px">
    <li>Final deliverable presentation</li>
    <li>Implementation support</li>
    <li>Knowledge transfer</li>
    <li>Impact measurement framework</li>
  </ul>

  <div class="phase-pill" style="left:377px;top:854px;padding-left:46px">Phase 6: Evolution &amp; Growth</div>
  <div class="phase-number" style="left:369px;top:852px">6</div>
  <h4 class="phase-sub" style="left:423px;top:894px">Sustaining Long-term Success</h4>
  <ul class="phase-list" style="left:421px;top:914px;width:250px">
    <li>Project success celebration</li>
    <li>Future opportunities exploration</li>
    <li>Partnership evolution planning</li>
    <li>Continuous improvement recommendations</li>
  </ul>
</main>
</body>
</html>
```